Australian Web Design company needs a business card design

We need a business card design for a Sydney based Web Design/Development company called "Tall Pine Web Design". We design, build and deploy websites for small to medium sized businesses. The final design should be clean and communicate that we are a professional and supportive company.
I'd like the Icon to be abstract. Something that embodies the power of the internet, needs to be clean/professional and show that we are human and that we support our customers. Hope that helps.
Target Market(s)
All small to medium businesses
Industry/Entity Type
Business
Contact Information for Business Card
Martin Forbes
Tall Pine Web Design
17 Wattle Grove Road
West Kelsworth
NSW 2250
0438 527 064
martin@tallpinewebdesign.com.au
www.tallpinewebdesign.com.au

```html
<!DOCTYPE html>
<html lang="en">
<head>
<meta charset="utf-8">
<title>Tall Pine Web Design – Business Card</title>
<link rel="stylesheet" href="https://fonts.googleapis.com/css2?family=Roboto+Condensed:wght@400;700&display=swap">
<style>
  :root {
    --backdrop: #8e8e8e;
    --card-light: #f1f1f1;
    --card-light-shade: #d4d4d4;
    --card-dark: #22252b;
    --brand-red: #ee2d2d;
    --ink-grey: #c9c9c9;
  }
  * { margin: 0; padding: 0; box-sizing: border-box; }
  html, body { width: 1200px; height: 800px; overflow: hidden; }
  body {
    background: var(--backdrop);
    font-family: "Roboto Condensed", sans-serif;
    position: relative;
  }
  .card {
    position: absolute;
    width: 500px;
    height: 286px;
    border-radius: 18px;
    overflow: hidden;
  }
  .card-front {
    left: 70px; top: 130px;
    background: radial-gradient(circle at 55% 55%, #ffffff 0%, var(--card-light) 45%, var(--card-light-shade) 100%);
  }
  .card-back {
    left: 630px; top: 130px;
    background: var(--card-dark);
  }
  .front-accent {
    position: absolute;
    right: -70px; top: -110px;
    width: 260px; height: 260px;
    border-radius: 50%;
    background: var(--brand-red);
  }
  .front-wordmark {
    position: absolute;
    left: 30px; top: 34px;
    display: flex; align-items: center; gap: 8px;
    color: var(--brand-red);
    font-weight: 700;
    font-size: 19px;
    text-transform: uppercase;
  }
  .wordmark-dot {
    width: 22px; height: 22px; border-radius: 50%;
    background: var(--brand-red);
  }
  .contact-block {
    position: absolute;
    left: 30px; bottom: 30px;
    border-left: 2px solid var(--brand-red);
    padding-left: 14px;
    color: var(--brand-red);
  }
  .contact-name {
    font-size: 30px;
    font-weight: 400;
    margin-bottom: 8px;
  }
  .contact-line {
    display: flex; align-items: center; gap: 8px;
    font-size: 15px;
    line-height: 23px;
  }
  .contact-line svg { width: 13px; height: 13px; flex: none; }
  .back-lockup {
    position: absolute;
    left: 0; right: 0; top: 92px;
    display: flex; justify-content: center; align-items: center; gap: 12px;
    color: var(--brand-red);
    font-weight: 700;
    font-size: 34px;
    text-transform: uppercase;
  }
  .back-lockup .wordmark-dot { width: 36px; height: 36px; }
  .back-url {
    position: absolute;
    left: 0; right: 0; top: 178px;
    text-align: center;
    color: var(--ink-grey);
    font-size: 15px;
    letter-spacing: 4px;
    text-transform: uppercase;
  }
  .brand-lockup {
    position: absolute;
    right: 60px; top: 640px;
    display: flex; align-items: center; gap: 14px;
    color: var(--brand-red);
    font-weight: 700;
    font-size: 46px;
    text-transform: uppercase;
  }
  .brand-lockup .wordmark-dot { width: 70px; height: 70px; }
</style>
</head>
<body>

  <section class="card card-front">
    <div class="front-accent"></div>
    <div class="front-wordmark"><span class="wordmark-dot"></span>Tall Pine Web Design</div>
    <div class="contact-block">
      <p class="contact-name">Martin Forbes</p>
      <p class="contact-line">
        <svg viewBox="0 0 12 12"><path d="M6 0.5a4 4 0 0 0-4 4c0 3 4 7 4 7s4-4 4-7a4 4 0 0 0-4-4z" fill="currentColor"/><circle cx="6" cy="4.5" r="1.5" fill="#fff"/></svg>
        17 Wattle Grove Road West Kelsworth NSW 2250
      </p>
      <p class="contact-line">
        <svg viewBox="0 0 12 12"><rect x="1" y="1" width="10" height="10" rx="2" fill="currentColor"/><path d="M4 3.2c.6 2.4 2.2 4 4.6 4.6l.6-1.1-1.4-.7-.6.6c-.9-.4-1.5-1-1.9-1.9l.6-.6-.7-1.4z" fill="#fff"/></svg>
        0438 527 064
      </p>
      <p class="contact-line">
        <svg viewBox="0 0 12 12" fill="none" stroke="currentColor" stroke-width="1"><circle cx="6" cy="6" r="5"/><ellipse cx="6" cy="6" rx="2.2" ry="5"/><path d="M1 6h10M2 3.5h8M2 8.5h8"/></svg>
        martin@tallpinewebdesign.com.au
      </p>
    </div>
  </section>

  <section class="card card-back">
    <div class="back-lockup"><span class="wordmark-dot"></span>Tall Pine Web Design</div>
    <p class="back-url">www.tallpinewebdesign.com.au</p>
  </section>

  <div class="brand-lockup"><span class="wordmark-dot"></span>Tall Pine Web Design</div>

</body>
</html>
```